Orbell Consulting- executive coaching business

looking for business card design for a newly started coaching business.
specialising in Exective coaching, Leadership, NLP and Motivation.
Looking for a simple, classy design using the existing logo attached and colour themes that complement the logo.
No red or orange in the business card design please.

Target Market(s)

Defence and Veteran community

Industry/Entity Type

Life Coaching

Contact Information for Business Card

looking for business cards for newly started coaching business.
specialising in Exective Coaching, Leadership, NLP and Motivation

Font styles to use
Serif
Script

Colors
0556a4
3176b5
86cfc6
33b8a4

Requirements
Must have
• Logo
• Email address- Jess@orbellconsulting.com.au
• Contact number
• Services provided - Executive Coaching, Leadership, NLP and Motivational Mapping.
Nice to have
• Same colours as logo
Should not have
• Red or orange

```html
<!DOCTYPE html>
<html lang="en">
<head>
<meta charset="utf-8">
<title>Orbell Consulting – Business Card</title>
<link rel="stylesheet" href="https://fonts.googleapis.com/css2?family=Open+Sans:ital,wght@0,400;0,600;0,700;1,700&display=swap">
<style>
  :root {
    --bg: #e9e7e8;
    --card: #ffffff;
    --brand-blue: #0556a4;
    --mid-blue: #3176b5;
    --green: #33b8a4;
    --text-grey: #5a5a5a;
    --rule-grey: #9a9a9a;
  }
  * { box-sizing: border-box; margin: 0; padding: 0; }
  html, body { width: 1200px; height: 799px; overflow: hidden; }
  body {
    background: var(--bg);
    font-family: "Open Sans", Arial, sans-serif;
    position: relative;
  }
  .card {
    position: absolute;
    top: 250px;
    width: 525px;
    height: 300px;
    background: var(--card);
    box-shadow: 0 2px 8px rgba(0,0,0,0.12);
    overflow: hidden;
  }
  .card--front { left: 45px; }
  .card--back { left: 630px; }

  .brand {
    display: flex;
    align-items: center;
    justify-content: center;
    gap: 12px;
  }
  .brand-name {
    font-weight: 600;
    font-size: 30px;
    color: var(--brand-blue);
    text-transform: uppercase;
    letter-spacing: 0.5px;
    white-space: nowrap;
  }
  .brand-dot {
    width: 44px; height: 44px;
    border: 2px solid var(--rule-grey);
    border-radius: 50%;
  }

  /* front */
  .card--front .brand { position: absolute; top: 48px; left: 0; right: 0; }
  .person {
    position: absolute;
    top: 128px; right: 36px;
    text-align: right;
  }
  .person-name { font-weight: 700; font-size: 17px; color: var(--brand-blue); }
  .person-role { font-size: 12px; color: var(--text-grey); }
  .contact {
    position: absolute;
    left: 36px; top: 178px;
    font-size: 11.5px;
    line-height: 1.55;
    color: var(--text-grey);
    white-space: nowrap;
  }
  .contact .sep { color: var(--brand-blue); padding: 0 4px; }
  .band {
    position: absolute;
    left: 0; right: 0; bottom: 22px;
    height: 16px;
    background: var(--brand-blue);
    border-top: 3px solid var(--mid-blue);
  }

  /* back */
  .card--back .brand { margin-top: 92px; }
  .services {
    text-align: center;
    margin-top: 14px;
  }
  .services-label { font-weight: 700; font-style: italic; font-size: 12px; color: var(--brand-blue); }
  .services-list { font-weight: 700; font-style: italic; font-size: 12.5px; color: var(--brand-blue); margin-top: 2px; }
  .services-web { font-size: 11.5px; color: var(--green); margin-top: 4px; }
</style>
</head>
<body>
  <section class="card card--front">
    <div class="brand">
      <span class="brand-name">Orbell Consulting</span>
      <span class="brand-dot"></span>
    </div>
    <div class="person">
      <div class="person-name">Dana Whitlow</div>
      <div class="person-role">President</div>
    </div>
    <div class="contact">
      <p>P: 610.482.3307<span class="sep">|</span>C: 610.482.3318<span class="sep">|</span>F: 610.482.3329<span class="sep">|</span>E: Jess@orbellconsulting.com.au</p>
      <p>No. 48, Harbour Lane, Newtown, Australia</p>
      <p>www.orbellconsulting.com.au</p>
    </div>
    <div class="band"></div>
  </section>

  <section class="card card--back">
    <div class="brand">
      <span class="brand-name">Orbell Consulting</span>
      <span class="brand-dot"></span>
    </div>
    <div class="services">
      <p class="services-label">- Services provided -</p>
      <p class="services-list">Executive Coaching, Leadership, NLP and Motivational Mapping.</p>
      <p class="services-web">www.orbellconsulting.com.au</p>
    </div>
  </section>
</body>
</html>
```